Psychology practice - information brochure/flyer - half A4 page folded (4 sides)

We need a brochure/flyer to market our psychology service to GPs (Doctors). We need to demonstrate to the doctors that we are the right choice for their patients, and that we cover a large range of services so all of their patients needs are met. We will demonstrate this by listing our range of services and our team of psychologists. We have two locations in Sydney and offer high end services. I've attached our company logo but we remain flexible regarding the style of the brochures. I will provide more details (services, locations & psychologist credentials) once our preferred brochure design has been selected.

```html
<!DOCTYPE html>
<html lang="en">
<head>
<meta charset="utf-8">
<title>Clearpath Psychology – Practice Information</title>
<link rel="stylesheet" href="https://fonts.googleapis.com/css2?family=Arimo:wght@400;700&display=swap">
<style>
:root{
  --grey:#6d6e70;
  --yellow:#f8bf1b;
  --teal:#5bc0cf;
  --cream:#fdf6e3;
  --ink:#2f3237;
  --white:#ffffff;
}
*{margin:0;padding:0;box-sizing:border-box}
html,body{width:835px;height:1200px;overflow:hidden;background:var(--white)}
body{font-family:"Arimo",Arial,sans-serif;color:var(--ink)}
.flyer{position:relative;width:835px;height:1200px;overflow:hidden}
.block{position:absolute}
.clinicians-panel{left:0;top:0;width:405px;height:496px;background:var(--grey)}
.services-panel{left:405px;top:0;width:430px;height:547px;background:var(--yellow);z-index:2}
.fees-band{left:0;top:496px;width:835px;height:194px;background:var(--teal)}
.clients-panel{left:0;top:690px;width:405px;height:510px;background:var(--grey)}
.hours-panel{left:405px;top:690px;width:430px;height:255px;background:var(--cream)}
.contact-panel{left:405px;top:945px;width:430px;height:255px;background:var(--teal)}
.heading{font-weight:700;font-size:20.5px;line-height:1}
.clinicians{left:63px;top:59px;color:var(--white);z-index:3}
.clinician{margin-top:22px}
.clinician-name{font-weight:700;font-size:15.5px;line-height:1.2}
.clinician-creds{font-size:12px;line-height:1.55;margin-top:3px}
.services{left:460px;top:59px;z-index:3}
.service-list{list-style:none;margin-top:14px;font-size:13.5px;line-height:17.5px}
.service-list li::before{content:"• "}
.fees{left:63px;top:505px;z-index:3;color:var(--ink)}
.fee-group{margin-top:11px}
.fee-group + .fee-group{margin-top:20px}
.fee-title{font-weight:700;font-size:14.5px;line-height:18px}
.fee-line{font-size:14.5px;line-height:19px}
.clients{left:63px;top:705px;color:var(--white)}
.client-list{list-style:none;margin-top:27px;font-size:15px;line-height:25px;width:210px}
.client-list li{padding-left:10px;text-indent:-10px}
.client-list li::before{content:"• "}
.hours{left:405px;top:800px;width:420px;text-align:center;font-weight:700;font-size:21.5px;line-height:29px;color:var(--ink)}
.hours-title{font-size:21.5px}
.appointments{left:405px;top:1006px;width:420px;text-align:center;font-weight:700;font-size:14.5px;line-height:20px;color:var(--ink)}
.address-lines{left:405px;top:1052px;width:420px;text-align:center;font-weight:700;font-size:14.5px;line-height:19.5px;color:var(--ink)}
.phone-line{font-size:18.5px;line-height:26px;margin-top:4px}
.ribbon{left:0;top:1003px;width:440px;height:67px;z-index:2}
.ribbon-text{left:70px;top:1014px;z-index:3;font-weight:700;font-size:21.5px;line-height:27px;color:var(--ink)}
.icon{z-index:4}
</style>
</head>
<body>
<main class="flyer">
  <div class="block clinicians-panel"></div>
  <div class="block services-panel"></div>
  <div class="block fees-band"></div>
  <div class="block clients-panel"></div>
  <div class="block hours-panel"></div>
  <div class="block contact-panel"></div>

  <section class="block clinicians">
    <h2 class="heading">Our Clinicians</h2>
    <div class="clinician"><p class="clinician-name">Dr Helena Marlow</p><p class="clinician-creds">D ClinPsych, MA, BSc (Psych), BPsych (Hons)</p></div>
    <div class="clinician"><p class="clinician-name">Dr Thomas Edward Crane</p><p class="clinician-creds">DPhil (Psych), BA-Psych (Hons),<br>GradDipEd, GDipMgt, MAPS, FCOP</p></div>
    <div class="clinician"><p class="clinician-name">Clara Benning</p><p class="clinician-creds">MPsych (Clin), BPsych (Hons)</p></div>
    <div class="clinician"><p class="clinician-name">Anisa Rahman</p><p class="clinician-creds">BPsych (Hons), GDipPsych</p></div>
    <div class="clinician"><p class="clinician-name">Dr Mira Haddad</p><p class="clinician-creds">D ClinPsych, MSc (Psych),<br>B Psych (Hons), MACPA, MAPS</p></div>
  </section>

  <section class="block services">
    <h2 class="heading">Type of Services we provide:</h2>
    <ul class="service-list">
      <li>Anxiety</li><li>Depression</li><li>Attention Deficit Hyperactivity Disorder (ADHD)</li><li>Phobias</li><li>Autism Spectrum Disorder</li><li>Intellectual disability</li><li>Learning difficulties</li><li>Bullying</li><li>Study stress</li><li>Procrastination</li><li>WorkCover</li><li>Stress management</li><li>Rehabilitation psychology</li><li>Addiction and relapse prevention</li><li>Anger management</li><li>Divorce/separation</li><li>Pregnancy</li><li>Trauma</li><li>Post-Traumatic Stress Disorder (PTSD)</li><li>Couples/Family Therapy</li><li>Domestic Violence</li><li>Non-Suicidal Self Injury</li><li>Grief and loss</li><li>Eating disorders / body image</li>
    </ul>
  </section>

  <section class="block fees">
    <h2 class="heading">Our Fee Structure</h2>
    <div class="fee-group">
      <p class="fee-title">Business Hours – 9am to 5pm</p>
      <p class="fee-line">• $150 per session for General Psychologist, with Medicare Rebate of $84.80</p>
      <p class="fee-line">• $190 per session for Clinical Psychologist, with Medicare Rebate of $124.50</p>
    </div>
    <div class="fee-group">
      <p class="fee-title">Out of Hours – weekends and after 5pm</p>
      <p class="fee-line">• $170 per session for General Psychologist, with Medicare Rebate of $84.80</p>
      <p class="fee-line">• $210 per session for Clinical Psychologist, with Medicare Rebate of $124.50</p>
    </div>
  </section>

  <section class="block clients">
    <h2 class="heading">Our Client Groups:</h2>
    <ul class="client-list">
      <li>Children 5-12</li><li>Adolescents</li><li>Adults</li><li>Veterans</li><li>Victims of crime</li><li>Injured workers</li><li>Culturally and Linguistically Diverse backgrounds</li><li>Refugees</li>
    </ul>
  </section>

  <svg class="block ribbon" width="440" height="67" viewBox="0 0 440 67" aria-hidden="true">
    <polygon points="0,0 440,0 416,33.5 440,67 0,67" fill="var(--yellow)"/>
  </svg>
  <p class="block ribbon-text">New location opening soon<br>in Calder St Westbrook</p>

  <section class="block hours">
    <h2 class="hours-title">Hours of Operation</h2>
    <p>Monday – Friday: 8am-6pm</p>
    <p>Saturday: 9am – 1pm</p>
  </section>

  <p class="block appointments">To Make Appointments<br>Please Contact us on below</p>
  <div class="block address-lines">
    <p>Westbrook - Shop 4, 27 Calder Street, 2048</p>
    <p>Lindfield Park - Suite 3, 8 Orchard Street, 2210</p>
    <p>e-mail: info@clearpathpsychology.com.au</p>
    <p>www.clearpathpsychology.com.au</p>
    <p class="phone-line">ph. 02 5550 1234 fax. 02 5550 1235</p>
  </div>

  <svg class="block icon" style="left:280px;top:176px" width="96" height="96" role="img" aria-label="Icon of a male doctor">
    <circle cx="48" cy="48" r="45" fill="var(--yellow)" stroke="var(--white)" stroke-width="4"/>
  </svg>
  <svg class="block icon" style="left:280px;top:310px" width="96" height="96" role="img" aria-label="Icon of a female doctor">
    <circle cx="48" cy="48" r="45" fill="var(--teal)" stroke="var(--white)" stroke-width="4"/>
  </svg>
  <svg class="block icon" style="left:670px;top:188px" width="98" height="98" role="img" aria-label="Icon of a checklist">
    <circle cx="49" cy="49" r="46" fill="var(--teal)" stroke="var(--white)" stroke-width="4"/>
  </svg>
  <svg class="block icon" style="left:628px;top:564px" width="96" height="96" role="img" aria-label="Icon of a hand holding banknotes">
    <circle cx="48" cy="48" r="45" fill="var(--grey)" stroke="var(--white)" stroke-width="4"/>
  </svg>
  <svg class="block icon" style="left:268px;top:786px" width="96" height="96" role="img" aria-label="Icon of a group of people">
    <circle cx="48" cy="48" r="45" fill="var(--yellow)" stroke="var(--white)" stroke-width="4"/>
  </svg>
  <svg class="block icon" style="left:568px;top:697px" width="96" height="96" role="img" aria-label="Icon of a clinician in scrubs">
    <circle cx="48" cy="48" r="45" fill="var(--teal)" stroke="var(--white)" stroke-width="4"/>
  </svg>
  <svg class="block icon" style="left:568px;top:902px" width="96" height="96" role="img" aria-label="Icon of a consultation at a desk">
    <circle cx="48" cy="48" r="45" fill="var(--yellow)" stroke="var(--white)" stroke-width="4"/>
  </svg>
</main>
</body>
</html>
```